KORVELLA Corporate Business Card

Modern business card design for company which focuses in the areas of Staffing, IT Consulting & Data Services. Please note: We are no longer using the IT subscript on the logo. All designs should have IT subscript removed.
Website: www.korvellait.example

```html
<!DOCTYPE html>
<html lang="en">
<head>
<meta charset="utf-8">
<title>KORVELLA Corporate Business Card</title>
<link href="https://fonts.googleapis.com/css2?family=Open+Sans:wght@400;600;700&display=swap" rel="stylesheet">
<style>
  :root {
    --stage: #333336;
    --card-white: #ffffff;
    --card-dark: #2a2a2c;
    --blue: #1e8fd6;
    --blue-deep: #175fa0;
    --blue-light: #29a8e0;
    --ink: #3d3d3d;
    --ink-soft: #7a7a7a;
  }
  * { box-sizing: border-box; margin: 0; padding: 0; }
  html, body { width: 1200px; height: 900px; overflow: hidden; }
  body {
    background: var(--stage);
    font-family: "Open Sans", Arial, sans-serif;
    position: relative;
  }
  .card { position: absolute; border-radius: 26px; overflow: hidden; }

  /* front */
  .card-front {
    left: 90px; top: 150px; width: 340px; height: 595px;
    background: var(--card-white);
  }
  .holder { position: absolute; left: 30px; top: 34px; padding-left: 16px; }
  .holder::before {
    content: ""; position: absolute; left: 0; top: 2px;
    width: 6px; height: 36px; background: var(--blue-deep);
  }
  .holder-name { color: var(--blue); font-weight: 600; font-size: 20px; letter-spacing: 0.5px; line-height: 1.1; }
  .holder-role { color: var(--ink-soft); font-size: 12px; }
  .brand-front {
    position: absolute; left: 30px; top: 140px;
    display: flex; align-items: center; gap: 10px;
  }
  .brand-mark { width: 26px; height: 26px; background: var(--blue-deep); }
  .brand-name { color: var(--blue); font-weight: 700; font-size: 46px; letter-spacing: 1px; line-height: 1; }
  .pixel-cluster {
    position: absolute; left: 160px; top: 205px; width: 140px; height: 105px;
    background: linear-gradient(135deg, var(--blue-deep), var(--blue-light));
    border-radius: 4px; opacity: 0.85;
  }
  .frame { position: absolute; left: 0; top: 0; }
  .contact {
    position: absolute; left: 60px; top: 345px;
    color: var(--ink); font-size: 15px; line-height: 1.6;
    list-style: none;
  }
  .contact li { display: flex; align-items: center; gap: 8px; }
  .contact .gap { padding-left: 20px; }
  .contact svg { flex: none; }

  /* back */
  .card-back {
    left: 520px; top: 280px; width: 595px; height: 340px;
    background: var(--card-dark);
    display: flex; align-items: center; justify-content: center;
  }
  .pixel-field {
    position: absolute; left: 150px; top: 60px; width: 320px; height: 220px;
    background: radial-gradient(ellipse at center, rgba(255,255,255,0.08), rgba(255,255,255,0.02) 70%, transparent);
  }
  .brand-back { position: relative; display: flex; align-items: center; gap: 14px; }
  .brand-back .brand-mark { width: 34px; height: 34px; background: var(--blue); }
  .brand-back .brand-name { font-size: 64px; }
</style>
</head>
<body>
  <section class="card card-front">
    <div class="holder">
      <p class="holder-name">DANIEL BROOKS</p>
      <p class="holder-role">Director</p>
    </div>
    <div class="brand-front">
      <span class="brand-mark"></span>
      <span class="brand-name">KORVELLA</span>
    </div>
    <div class="pixel-cluster" role="img" aria-label="Cluster of scattered blue squares"></div>
    <svg class="frame" width="340" height="595" viewBox="0 0 340 595" aria-hidden="true">
      <path d="M140 300 H75 Q37 300 37 338 V528 Q37 566 75 566 H265 Q303 566 303 528 V338 Q303 300 280 300"
            fill="none" stroke="var(--blue)" stroke-width="14" stroke-linecap="square"/>
    </svg>
    <ul class="contact">
      <li class="gap">48 Harbor Lane</li>
      <li class="gap">Millbrook, OH 43210</li>
      <li>
        <svg width="12" height="12" viewBox="0 0 12 12"><path d="M2 1 L4.5 1 L5.5 3.5 L4 4.5 Q5 7 7.5 8 L8.5 6.5 L11 7.5 L11 10 Q6 11 1 5 Z" fill="var(--blue)"/></svg>
        555-014-2290
      </li>
      <li>
        <svg width="12" height="12" viewBox="0 0 12 12"><rect x="1" y="2.5" width="10" height="7" fill="none" stroke="var(--blue)" stroke-width="1.3"/><path d="M1 2.5 L6 6.5 L11 2.5" fill="none" stroke="var(--blue)" stroke-width="1.3"/></svg>
        contactus@korvellait.example
      </li>
      <li>
        <svg width="12" height="12" viewBox="0 0 12 12"><circle cx="6" cy="6" r="5" fill="none" stroke="var(--blue)" stroke-width="1.3"/><path d="M1 6 H11 M6 1 Q3 6 6 11 M6 1 Q9 6 6 11" fill="none" stroke="var(--blue)" stroke-width="1"/></svg>
        www.korvellait.example
      </li>
    </ul>
  </section>

  <section class="card card-back">
    <div class="pixel-field" role="img" aria-label="Faint field of scattered grey squares"></div>
    <div class="brand-back">
      <span class="brand-mark"></span>
      <span class="brand-name">KORVELLA</span>
    </div>
  </section>
</body>
</html>
```